Adult Job Portal needs a Web Design

We need a web design for a landing and search page for an ADULT-JOB-portal.

The structure of landing page can be taken from tumblewithpals.com.

The structure of job search page can be taken from: http://www.vacancyquarrel.co.uk/

Users should be able to recognize that is a SEX-INDUSTRY job portal.

The project name can not be published for ... some reasons.
Updates

Hi, Pinnlers.

Please note: the project was upgraded to "Guaranteed"
Thanks in advance for great work.
BR. M.

Hi ArtPinnlers,
please find attached the landing page wireframe.
It should make it easier for you to know what is expected.
Thanks in advance, guys!

Target Market(s)

women 18 to 30 years old

Industry/Entity Type

Adult

Requirements
Must have
• We expect to get design for the following pages:
- Landing page
- Add profile (name, description, photos, skills, preferable location)
- Job search with filters (example http://www.vacancyquarrel.co.uk/jobs)
- Companies list (example http://www.vacancyquarrel.co.uk/companies-in-oxfordshire)
- Company page (example http://www.vacancyquarrel.co.uk/company/velquin)
Should not have
• pornography, violence

```html
<!DOCTYPE html>
<html lang="en">
<head>
<meta charset="utf-8">
<title>Job Search</title>
<link rel="stylesheet" href="https://fonts.googleapis.com/css2?family=Jost:wght@500&family=Questrial&display=swap">
<style>
  :root {
    --brand: #f4384f;
    --ink: #6b6b6b;
    --ink-soft: #8a8a8a;
    --line: #c9c9c9;
    --card: #f8f8f8;
    --pager: #f1f1f1;
    --icon: #6e6e6e;
    --white: #ffffff;
  }
  * { box-sizing: border-box; margin: 0; padding: 0; }
  html, body { width: 1200px; height: 1098px; overflow: hidden; background: var(--white); }
  body { position: relative; font-family: "Questrial", sans-serif; color: var(--ink); letter-spacing: 1.2px; }

  .site-header { position: absolute; left: 0; top: 0; width: 1200px; height: 90px; background: var(--brand); }
  .site-name { position: absolute; left: 82px; top: 12px; font-family: "Jost", sans-serif; font-weight: 500; font-size: 58px; letter-spacing: 3px; color: var(--white); line-height: 64px; }

  .search-bar { position: absolute; left: 0; top: 111px; width: 1200px; height: 66px; border-bottom: 1px solid var(--line); }
  .search-field { position: absolute; top: 0; width: 396px; height: 44px; border: 1px solid var(--line); padding-left: 16px; font-size: 21px; line-height: 42px; color: var(--ink-soft); }
  .search-field--what { left: 83px; }
  .search-field--where { left: 495px; }
  .search-button { position: absolute; left: 909px; top: 0; width: 200px; height: 44px; background: var(--brand); color: var(--white); font-size: 20px; letter-spacing: 2.5px; text-align: center; line-height: 44px; font-weight: bold; }

  .sidebar { position: absolute; left: 0; top: 178px; width: 352px; height: 856px; border-right: 1px solid var(--line); }
  .sidebar-title { position: absolute; left: 84px; top: 12px; font-size: 32px; font-style: italic; color: var(--ink-soft); letter-spacing: 2px; }
  .filter-group { position: absolute; left: 83px; width: 269px; }
  .filter-heading { height: 44px; background: var(--brand); color: var(--white); font-size: 17px; line-height: 44px; padding-left: 13px; }
  .filter-options { list-style: none; padding: 11px 0 0 20px; }
  .filter-option { display: flex; align-items: center; height: 33px; font-size: 19px; color: var(--ink-soft); }
  .checkbox { width: 22px; height: 22px; border: 1.5px solid var(--line); border-radius: 5px; margin-right: 13px; }

  .results { position: absolute; left: 366px; top: 178px; width: 748px; }
  .results-count { position: absolute; left: 2px; top: 20px; font-size: 33px; color: var(--ink-soft); letter-spacing: 2px; }
  .job-list { list-style: none; position: absolute; top: 73px; left: 0; }
  .job-card { position: relative; width: 748px; height: 107px; margin-bottom: 4.5px; background: var(--card); border-left: 6px solid var(--brand); }
  .job-thumb { position: absolute; left: 34px; top: 9px; width: 60px; height: 89px; background: linear-gradient(180deg, #7a7a7a, #626262); border-radius: 30px 30px 8px 8px; }
  .job-info { position: absolute; left: 131px; top: 10px; }
  .job-title { font-size: 23px; letter-spacing: 2px; color: var(--ink); text-decoration: underline; text-underline-offset: 4px; text-decoration-thickness: 1px; line-height: 30px; }
  .job-meta { font-size: 18px; line-height: 25px; color: var(--ink); }
  .job-date { color: var(--brand); }
  .job-actions { position: absolute; right: 20px; top: 38px; display: flex; gap: 20px; }
  .job-actions svg { width: 32px; height: 30px; fill: var(--brand); }

  .pager { position: absolute; left: 598px; top: 956px; display: flex; gap: 4px; list-style: none; }
  .pager-item { height: 44px; min-width: 44px; background: var(--pager); color: var(--brand); font-size: 21px; line-height: 44px; text-align: center; }
  .pager-item--wide { width: 66px; }
  .pager-item--current { background: var(--brand); color: var(--white); }
  .pager-item svg { width: 14px; height: 14px; stroke: var(--brand); fill: none; stroke-width: 3; vertical-align: -1px; }

  .site-footer { position: absolute; left: 0; top: 1034px; width: 1200px; height: 64px; border-top: 1px solid var(--line); text-align: center; font-size: 19px; line-height: 66px; color: var(--ink); letter-spacing: 2px; }
</style>
</head>
<body>
  <header class="site-header"><div class="site-name">LOGO</div></header>

  <div class="search-bar">
    <div class="search-field search-field--what">What</div>
    <div class="search-field search-field--where">Where</div>
    <div class="search-button">SEARCH</div>
  </div>

  <aside class="sidebar">
    <h2 class="sidebar-title">Filter by</h2>
    <section class="filter-group" style="top:73px">
      <div class="filter-heading">Employment type</div>
      <ul class="filter-options">
        <li class="filter-option"><span class="checkbox"></span>Contract</li>
        <li class="filter-option"><span class="checkbox"></span>Temporary</li>
        <li class="filter-option"><span class="checkbox"></span>Part time</li>
        <li class="filter-option"><span class="checkbox"></span>Full time</li>
      </ul>
    </section>
    <section class="filter-group" style="top:281px">
      <div class="filter-heading">Employment type</div>
      <ul class="filter-options">
        <li class="filter-option"><span class="checkbox"></span>Contract</li>
        <li class="filter-option"><span class="checkbox"></span>Temporary</li>
        <li class="filter-option"><span class="checkbox"></span>Part time</li>
        <li class="filter-option"><span class="checkbox"></span>Full time</li>
      </ul>
    </section>
    <section class="filter-group" style="top:494px">
      <div class="filter-heading">Employment type</div>
      <ul class="filter-options">
        <li class="filter-option"><span class="checkbox"></span>Contract</li>
        <li class="filter-option"><span class="checkbox"></span>Temporary</li>
        <li class="filter-option"><span class="checkbox"></span>Part time</li>
        <li class="filter-option"><span class="checkbox"></span>Full time</li>
      </ul>
    </section>
  </aside>

  <main class="results">
    <h1 class="results-count">2034 Jobs</h1>
    <ul class="job-list">
      <li class="job-card">
        <div class="job-thumb" role="img" aria-label="Employer emblem"></div>
        <div class="job-info">
          <div class="job-title">Vacancy Name</div>
          <div class="job-meta"><span class="job-date">29 Oct 2013</span>, Industry Name of Job</div>
          <div class="job-meta">night job &nbsp;|&nbsp; day job &nbsp;|&nbsp; keyword</div>
        </div>
        <div class="job-actions">
          <svg viewBox="0 0 32 30"><path d="M16 29 C6 21 1 16 1 9 C1 4 5 1 9 1 C12 1 14.5 3 16 5.5 C17.5 3 20 1 23 1 C27 1 31 4 31 9 C31 16 26 21 16 29Z"/></svg>
          <svg viewBox="0 0 32 30"><path d="M16 1 L20 11 L31 11.5 L22.5 18.5 L25.5 29 L16 23 L6.5 29 L9.5 18.5 L1 11.5 L12 11Z"/></svg>
        </div>
      </li>
      <li class="job-card">
        <div class="job-thumb" role="img" aria-label="Employer emblem"></div>
        <div class="job-info">
          <div class="job-title">Vacancy Name</div>
          <div class="job-meta"><span class="job-date">29 Oct 2013</span>, Industry Name of Job</div>
          <div class="job-meta">night job &nbsp;|&nbsp; day job &nbsp;|&nbsp; keyword</div>
        </div>
        <div class="job-actions">
          <svg viewBox="0 0 32 30"><path d="M16 29 C6 21 1 16 1 9 C1 4 5 1 9 1 C12 1 14.5 3 16 5.5 C17.5 3 20 1 23 1 C27 1 31 4 31 9 C31 16 26 21 16 29Z"/></svg>
          <svg viewBox="0 0 32 30"><path d="M16 1 L20 11 L31 11.5 L22.5 18.5 L25.5 29 L16 23 L6.5 29 L9.5 18.5 L1 11.5 L12 11Z"/></svg>
        </div>
      </li>
      <li class="job-card">
        <div class="job-thumb" role="img" aria-label="Employer emblem"></div>
        <div class="job-info">
          <div class="job-title">Vacancy Name</div>
          <div class="job-meta"><span class="job-date">29 Oct 2013</span>, Industry Name of Job</div>
          <div class="job-meta">night job &nbsp;|&nbsp; day job &nbsp;|&nbsp; keyword</div>
        </div>
        <div class="job-actions">
          <svg viewBox="0 0 32 30"><path d="M16 29 C6 21 1 16 1 9 C1 4 5 1 9 1 C12 1 14.5 3 16 5.5 C17.5 3 20 1 23 1 C27 1 31 4 31 9 C31 16 26 21 16 29Z"/></svg>
          <svg viewBox="0 0 32 30"><path d="M16 1 L20 11 L31 11.5 L22.5 18.5 L25.5 29 L16 23 L6.5 29 L9.5 18.5 L1 11.5 L12 11Z"/></svg>
        </div>
      </li>
      <li class="job-card">
        <div class="job-thumb" role="img" aria-label="Employer emblem"></div>
        <div class="job-info">
          <div class="job-title">Vacancy Name</div>
          <div class="job-meta"><span class="job-date">29 Oct 2013</span>, Industry Name of Job</div>
          <div class="job-meta">night job &nbsp;|&nbsp; day job &nbsp;|&nbsp; keyword</div>
        </div>
        <div class="job-actions">
          <svg viewBox="0 0 32 30"><path d="M16 29 C6 21 1 16 1 9 C1 4 5 1 9 1 C12 1 14.5 3 16 5.5 C17.5 3 20 1 23 1 C27 1 31 4 31 9 C31 16 26 21 16 29Z"/></svg>
          <svg viewBox="0 0 32 30"><path d="M16 1 L20 11 L31 11.5 L22.5 18.5 L25.5 29 L16 23 L6.5 29 L9.5 18.5 L1 11.5 L12 11Z"/></svg>
        </div>
      </li>
      <li class="job-card">
        <div class="job-thumb" role="img" aria-label="Employer emblem"></div>
        <div class="job-info">
          <div class="job-title">Vacancy Name</div>
          <div class="job-meta"><span class="job-date">29 Oct 2013</span>, Industry Name of Job</div>
          <div class="job-meta">night job &nbsp;|&nbsp; day job &nbsp;|&nbsp; keyword</div>
        </div>
        <div class="job-actions">
          <svg viewBox="0 0 32 30"><path d="M16 29 C6 21 1 16 1 9 C1 4 5 1 9 1 C12 1 14.5 3 16 5.5 C17.5 3 20 1 23 1 C27 1 31 4 31 9 C31 16 26 21 16 29Z"/></svg>
          <svg viewBox="0 0 32 30"><path d="M16 1 L20 11 L31 11.5 L22.5 18.5 L25.5 29 L16 23 L6.5 29 L9.5 18.5 L1 11.5 L12 11Z"/></svg>
        </div>
      </li>
      <li class="job-card">
        <div class="job-thumb" role="img" aria-label="Employer emblem"></div>
        <div class="job-info">
          <div class="job-title">Vacancy Name</div>
          <div class="job-meta"><span class="job-date">29 Oct 2013</span>, Industry Name of Job</div>
          <div class="job-meta">night job &nbsp;|&nbsp; day job &nbsp;|&nbsp; keyword</div>
        </div>
        <div class="job-actions">
          <svg viewBox="0 0 32 30"><path d="M16 29 C6 21 1 16 1 9 C1 4 5 1 9 1 C12 1 14.5 3 16 5.5 C17.5 3 20 1 23 1 C27 1 31 4 31 9 C31 16 26 21 16 29Z"/></svg>
          <svg viewBox="0 0 32 30"><path d="M16 1 L20 11 L31 11.5 L22.5 18.5 L25.5 29 L16 23 L6.5 29 L9.5 18.5 L1 11.5 L12 11Z"/></svg>
        </div>
      </li>
    </ul>
  </main>

  <ul class="pager">
    <li class="pager-item pager-item--wide">First</li>
    <li class="pager-item"><svg viewBox="0 0 14 14"><path d="M9 2 L4 7 L9 12"/></svg></li>
    <li class="pager-item">1</li>
    <li class="pager-item pager-item--current">2</li>
    <li class="pager-item">3</li>
    <li class="pager-item">4</li>
    <li class="pager-item">5</li>
    <li class="pager-item">6</li>
    <li class="pager-item"><svg viewBox="0 0 14 14"><path d="M5 2 L10 7 L5 12"/></svg></li>
    <li class="pager-item pager-item--wide">Last</li>
  </ul>

  <footer class="site-footer">Friendbook &nbsp;|&nbsp; chirper &nbsp;|&nbsp; Searchly +</footer>
</body>
</html>
```